Logo/ business card idea for a weld inspection/ nondestructive testing LLC

I have just started an LLC (my first) for weld inspection and non-destructive testing. I am the president and only member of this company. It is a very niche industry and word of mouth is basically the only advertisement needed to get you the next job. I will offer magnetic particle, dye penetrant, ultrasonic, and visual testing for the non-destructive services. X-ray is a form of non-destructive testing that I spent a few years doing but to costly for me at this time. All pipelines under the ground are welded, visually inspected and x-ray by someone just like me. All new building construction, any type of nuclear plant , pressure vessel, ect. , the welds are inspected by someone like me. Its is every increasing also with safety concerns. People are living right next to this stuff!!I will be the guy that fabrication shops or construction companies call to give the final OK that the welds are satisfactory after inspection to a certain code or standard. The designers have all the freedom they wish but I have attached a PDF with greater explanations and color ideas. I want raised glossy print on the front of the card and the necessary info. The back will not have raised print and serve more as a brief resume listing the certifications I have. The company only cares about the certifications and ultimately my signature. I want to make the front of the car into a fridge magnet to pass out with the card also. Something that is appealing to hang up instead of getting lost in someones wallet. The final design………. should be classic and stand the test of time. It should communicate precision and accuracy as well as incorporate the sound beam you will find in the PDF I’ve attached.Thanks and have a great day,Dale

Target Market(s)

Adult males in english speaking countries that handle welding and/or construction duties. Most of the time under heavy time constraints and deadlines. Ages 30-60

Industry/Entity Type

Construction

Contact Information for Business Card

Halvern Inspection Services, LLC
Dale Halvern
Ithaca, MI
989-514-2730
halv7dw@mailbreeze.net

Font styles to use
Other font styles liked:
• designers choice

Requirements
Nice to have
• The logo on the front can completely encase the Halvern, be segmented incorporating the Halvern, or next to it. There can also be a couple of “flaws” (the red, blue and yellow in some of the pictures attached in the PDF) in the sound beam spread.

```html
<!DOCTYPE html>
<html lang="en">
<head>
<meta charset="utf-8">
<title>Halvern Inspection Services, LLC – Business Card</title>
<link rel="stylesheet" href="https://fonts.googleapis.com/css2?family=Saira:wght@400;600;700&display=swap">
<style>
  :root {
    --page: #ffffff;
    --frame: #e2e2e2;
    --charcoal: #2b2a29;
    --slate: #b2b2b2;
    --gold-deep: #c9a45a;
    --gold-mid: #e3cc93;
    --gold-light: #f6ecd2;
    --white: #ffffff;
    --ink: #2f2f2f;
    --signal-red: #e31e24;
  }
  * { margin: 0; padding: 0; box-sizing: border-box; }
  html, body {
    width: 1047px; height: 1200px; overflow: hidden;
    background: var(--page);
    font-family: "Saira", sans-serif;
  }
  .sheet {
    position: relative; width: 1047px; height: 1200px;
    border: 3px solid var(--frame);
  }
  .card {
    position: absolute; left: 70px; width: 888px;
    box-shadow: 0 10px 14px rgba(0,0,0,0.28);
    overflow: hidden;
  }
  .card--front { top: 53px; height: 517px; }
  .card--back  { top: 614px; height: 514px; }
  .card__art { position: absolute; inset: 0; width: 100%; height: 100%; display: block; }

  .brand { position: absolute; color: var(--signal-red); font-weight: 600; line-height: 1; }
  .brand__name { display: block; font-size: 62px; letter-spacing: 1px; }
  .brand__tag  { display: block; font-size: 28px; margin-top: 2px; }
  .card--front .brand { left: 308px; top: 50px; }
  .card--back .brand  { left: 440px; top: 360px; }

  .contact { position: absolute; left: 54px; top: 262px; color: var(--white); }
  .contact__name { font-size: 29px; font-weight: 700; line-height: 1.2; }
  .contact__role { font-size: 21px; font-weight: 400; margin-top: 18px; }
  .contact__line { display: flex; align-items: center; gap: 10px; font-size: 23px; font-weight: 700; }
  .contact__line--phone { margin-top: 18px; }
  .contact__line--mail  { margin-top: 6px; }
  .contact__icon { width: 22px; height: 22px; flex: none; }

  .credentials { position: absolute; left: 48px; top: 50px; list-style: none; color: var(--ink); font-size: 24px; line-height: 45px; }
  .credentials li { position: relative; padding-left: 25px; }
  .credentials li::before {
    content: ""; position: absolute; left: 0; top: 19px;
    width: 8px; height: 8px; border-radius: 50%; background: var(--signal-red);
  }
  .credentials li.credentials__sub { padding-left: 133px; }
  .credentials li.credentials__sub::before { display: none; }
</style>
</head>
<body>
<main class="sheet">

  <section class="card card--front" aria-label="Business card front">
    <svg class="card__art" viewBox="0 0 708 412" preserveAspectRatio="none" aria-hidden="true">
      <defs>
        <linearGradient id="goldFront" x1="0" y1="0" x2="1" y2="1">
          <stop offset="0" stop-color="var(--gold-deep)"/>
          <stop offset="0.35" stop-color="var(--gold-light)"/>
          <stop offset="0.55" stop-color="var(--white)"/>
          <stop offset="0.8" stop-color="var(--gold-mid)"/>
          <stop offset="1" stop-color="var(--gold-light)"/>
        </linearGradient>
      </defs>
      <rect width="708" height="412" fill="var(--slate)"/>
      <path d="M97 0 L708 0 Q690 300 482 412 Z" fill="url(#goldFront)"/>
      <path d="M0 0 L97 0 L482 412 L0 412 Z" fill="var(--charcoal)"/>
    </svg>
    <div class="brand">
      <span class="brand__name">HALVERN</span>
      <span class="brand__tag">Inspection Services, LLC</span>
    </div>
    <div class="contact">
      <p class="contact__name">Dale Halvern</p>
      <p class="contact__role">AWQ Certified Welding Inspector</p>
      <p class="contact__line contact__line--phone">
        <svg class="contact__icon" viewBox="0 0 24 24" aria-hidden="true"><path fill="currentColor" d="M6.6 2.5l2.6 3.6-1.6 2c.9 2.6 3 5 5.8 6.6l2-1.5 3.6 2.5-1.5 3.3C11 19 4.6 12 3.6 4.3z"/></svg>
        989-514-2730
      </p>
      <p class="contact__line contact__line--mail">
        <svg class="contact__icon" viewBox="0 0 24 24" aria-hidden="true"><rect x="2" y="6" width="20" height="13" fill="none" stroke="currentColor" stroke-width="2"/><path d="M2 6l10 7 10-7" fill="none" stroke="currentColor" stroke-width="2"/></svg>
        halv7dw@mailbreeze.net
      </p>
    </div>
  </section>

  <section class="card card--back" aria-label="Business card back">
    <svg class="card__art" viewBox="0 0 708 410" preserveAspectRatio="none" aria-hidden="true">
      <defs>
        <linearGradient id="goldBack" x1="1" y1="0" x2="0" y2="1">
          <stop offset="0" stop-color="var(--gold-deep)"/>
          <stop offset="0.35" stop-color="var(--gold-light)"/>
          <stop offset="0.55" stop-color="var(--white)"/>
          <stop offset="0.8" stop-color="var(--gold-mid)"/>
          <stop offset="1" stop-color="var(--gold-light)"/>
        </linearGradient>
      </defs>
      <rect width="708" height="410" fill="var(--slate)"/>
      <path d="M0 0 L610 0 L228 410 Q20 300 0 0 Z" fill="url(#goldBack)"/>
      <path d="M610 0 L708 0 L708 410 L228 410 Z" fill="var(--charcoal)"/>
    </svg>
    <ul class="credentials">
      <li>AWQ Certified Welding Inspector</li>
      <li>AWQ Certified Radiographic Interpreter</li>
      <li>AWQ Certified Welding Educator</li>
      <li>Level II - Ultrasonic Testing</li>
      <li class="credentials__sub">Magnetic Particle Testing</li>
      <li class="credentials__sub">Liquid Penetrant Testing</li>
    </ul>
    <div class="brand">
      <span class="brand__name">HALVERN</span>
      <span class="brand__tag">Inspection Services, LLC</span>
    </div>
  </section>

</main>
</body>
</html>
```